Business Card Design

We are a Sydney based bespoke Concierge company, providing hospitality services including Concierge staffing, catering, home dining, events, delivery, passwright, and manage desks in residential apartment services. Our website goes into more detail.

Target Market(s)

corporate clients, upscale residential clients, executives,

Industry/Entity Type

Hospitality

Contact Information for Business Card

David SouthwellDirector of Operations & Customer Experience
Larkmoor Concierge
W:www.larkmoorconcierge.net;
E;martin@larkmoorconcierge.net
M: 0491 570 213

Font styles to use
Serif

Colors
3176b5
85cae6
d2a4cc
6b449b

Requirements
Must have
• Business name
• Name
• Title
• Tel
• Email
• Website
Nice to have
• Back - facebook , twitter, instagram

```html
<!DOCTYPE html>
<html lang="en">
<head>
<meta charset="utf-8">
<title>Larkmoor Concierge — Business Card</title>
<link rel="stylesheet" href="https://fonts.googleapis.com/css2?family=Open+Sans:wght@400;600;700&display=swap">
<style>
  :root {
    --stage: #2a2a2c;
    --sky: #1aa7e4;
    --sky-light: #3cc3f0;
    --sky-deep: #0a8fd0;
    --paper: #f2f2f3;
    --paper-shade: #d9d9dc;
    --ink: #2b2b2d;
    --ink-soft: #555;
    --white: #ffffff;
  }
  * { margin: 0; padding: 0; box-sizing: border-box; }
  html, body { width: 1200px; height: 660px; overflow: hidden; }
  body {
    background: var(--stage);
    font-family: "Open Sans", Arial, sans-serif;
    position: relative;
  }
  .card {
    position: absolute;
    top: 176px;
    width: 540px;
    height: 308px;
    border-radius: 3px;
    overflow: hidden;
    box-shadow: 0 10px 30px rgba(0,0,0,.45);
  }
  .card--back { left: 40px; background: linear-gradient(135deg, var(--sky-light), var(--sky-deep)); }
  .card--front { left: 620px; background: linear-gradient(110deg, var(--paper-shade), var(--white) 55%, var(--paper)); }
  .card__wave { position: absolute; inset: 0; }

  .brand {
    position: absolute;
    display: flex;
    align-items: center;
    gap: 10px;
    font-family: "Open Sans", Arial, sans-serif;
    font-weight: 600;
    white-space: nowrap;
  }
  .brand__square { width: 10px; height: 10px; background: currentColor; flex: none; }
  .brand--light { color: var(--white); }
  .brand--dark { color: var(--ink); }

  .card--back .brand { left: 60px; top: 118px; font-size: 30px; }
  .social { position: absolute; right: 60px; bottom: 62px; display: flex; gap: 10px; }
  .social__dot { width: 20px; height: 20px; border-radius: 50%; background: var(--white); }
  .card--back .site { position: absolute; right: 46px; bottom: 30px; color: var(--white); font-size: 14px; }

  .front__band {
    position: absolute; left: 0; top: 0; width: 100%; height: 150px;
    background: linear-gradient(90deg, var(--sky-deep), var(--sky-light) 60%, var(--sky));
  }
  .card--front .band-brand { left: 36px; top: 58px; font-size: 30px; }
  .role {
    position: absolute; left: 160px; top: 150px; height: 22px; right: 0;
    background: var(--sky); color: var(--white);
    font-size: 11px; font-weight: 700; letter-spacing: 1.2px; text-transform: uppercase;
    display: flex; align-items: center; padding-left: 16px;
  }
  .person { position: absolute; left: 34px; top: 188px; font-size: 20px; font-weight: 700; color: var(--ink); }
  .contacts { position: absolute; left: 34px; top: 230px; list-style: none; }
  .contacts li { display: flex; align-items: center; gap: 12px; font-size: 15px; color: var(--ink-soft); height: 22px; }
  .contacts li.phone { font-size: 19px; font-weight: 700; color: var(--ink); }
  .contacts svg { width: 16px; height: 16px; fill: none; stroke: var(--sky); stroke-width: 1.8; }
  .card--front .corner-brand { right: 30px; top: 214px; font-size: 16px; }
</style>
</head>
<body>
  <section class="card card--back" aria-label="Card back">
    <svg class="card__wave" viewBox="0 0 540 308" preserveAspectRatio="none" aria-hidden="true">
      <path d="M0 308 C120 300 150 180 260 150 C380 118 440 40 540 0 L540 308 Z" fill="#0c9ad8" opacity=".55"/>
    </svg>
    <div class="brand brand--light"><span class="brand__square"></span>Larkmoor Concierge</div>
    <div class="social"><span class="social__dot"></span><span class="social__dot"></span><span class="social__dot"></span></div>
    <div class="site">www.larkmoorconcierge.net</div>
  </section>

  <section class="card card--front" aria-label="Card front">
    <div class="front__band"></div>
    <div class="brand brand--light band-brand"><span class="brand__square"></span>Larkmoor Concierge</div>
    <div class="role">Director of Operations &amp; Customer Experience</div>
    <div class="person">Martin Ashgrove</div>
    <ul class="contacts">
      <li><svg viewBox="0 0 16 16"><circle cx="8" cy="8" r="6.5"/><path d="M1.5 8h13M8 1.5c3 3.5 3 9.5 0 13M8 1.5c-3 3.5-3 9.5 0 13"/></svg>www.larkmoorconcierge.net</li>
      <li><svg viewBox="0 0 16 16"><rect x="1.5" y="3.5" width="13" height="9" rx="1"/><path d="M1.5 4l6.5 5 6.5-5"/></svg>martin@larkmoorconcierge.net</li>
      <li class="phone"><svg viewBox="0 0 16 16"><circle cx="8" cy="8" r="6.5"/><path d="M6 5c0 3 2 5.5 5 6"/></svg>0491 570 213</li>
    </ul>
    <div class="brand brand--dark corner-brand"><span class="brand__square"></span>Larkmoor Concierge</div>
  </section>
</body>
</html>
```